Business Card Design

We need a basic, but modern design card. Our business is a local Queanbeyan/Canberra courier service, but can organise interstate delivery if needed. Our fleet ranges from 1 tonne vans to 8 tonne trucks.

Industry/Entity Type

Business

Contact Information for Business Card

Harbourline Freight
14 Wren Parade
Queanbeyan NSW 2620

Dean Fairley
CEO

Phone: 02 61847315
Fax: 02 61847358
email: dean@harbourlinefreight.example.au

```html
<!DOCTYPE html>
<html lang="en">
<head>
<meta charset="utf-8">
<title>Harbourline Freight – Business Card</title>
<link rel="stylesheet" href="https://fonts.googleapis.com/css2?family=Mulish:wght@300;400&family=Open+Sans:wght@400;600;700&display=swap">
<style>
  :root {
    --page-bg: #3a3a3a;
    --card-light: #ffffff;
    --card-dark: #1e1e1e;
    --brand-blue: #1ba1e2;
    --ink: #2b2b2b;
    --ink-soft: #444444;
    --map-light-a: #eeeeee;
    --map-light-b: #f8f8f8;
    --map-dark-a: #2a2a2a;
    --map-dark-b: #232323;
    --divider: #333333;
  }
  * { box-sizing: border-box; margin: 0; padding: 0; }
  html, body {
    width: 1200px; height: 964px; overflow: hidden;
    background: var(--page-bg);
  }
  .stage {
    position: relative; width: 1200px; height: 964px;
    display: flex; flex-direction: column; align-items: center; justify-content: center;
    gap: 44px;
  }
  .card {
    position: relative; width: 700px; height: 400px; overflow: hidden;
    box-shadow: 0 10px 30px rgba(0,0,0,.35);
  }
  .map-area {
    position: absolute; left: 6%; top: 8%; width: 88%; height: 78%;
    border-radius: 40% 45% 35% 40%;
  }
  /* Back */
  .card--back { background: var(--card-dark); }
  .card--back .map-area {
    background: radial-gradient(ellipse at center, var(--map-dark-a) 0%, var(--map-dark-b) 70%, transparent 100%);
  }
  .back-brand {
    position: absolute; left: 60px; bottom: 110px;
    font-family: "Mulish", sans-serif; font-weight: 300;
    font-size: 54px; color: var(--brand-blue); letter-spacing: .5px;
  }
  /* Front */
  .card--front { background: var(--card-light); }
  .card--front .map-area {
    background: radial-gradient(ellipse at center, var(--map-light-a) 0%, var(--map-light-b) 70%, transparent 100%);
  }
  .front-brand {
    position: absolute; left: 38px; top: 178px;
    font-family: "Mulish", sans-serif; font-weight: 300;
    font-size: 35px; color: var(--brand-blue);
  }
  .divider {
    position: absolute; left: 392px; top: 120px; width: 1.5px; height: 190px;
    background: var(--divider);
  }
  .contact {
    position: absolute; left: 412px; top: 112px;
    font-family: "Open Sans", sans-serif; color: var(--ink-soft);
  }
  .contact__name {
    font-size: 19px; font-weight: 700; color: var(--ink); letter-spacing: .3px;
  }
  .contact__name .surname { color: var(--brand-blue); }
  .contact__title { font-size: 13px; letter-spacing: .6px; margin-top: 1px; }
  .contact__row {
    display: flex; align-items: center; gap: 10px; margin-top: 16px;
    font-size: 12.5px; line-height: 1.35;
  }
  .contact__row:first-of-type { margin-top: 22px; }
  .contact__label { font-weight: 600; color: var(--ink); }
  .icon-badge {
    width: 30px; height: 30px; border-radius: 50%; flex: none;
    background: var(--brand-blue); display: flex; align-items: center; justify-content: center;
  }
  .address {
    position: absolute; left: 0; right: 0; bottom: 34px; text-align: center;
    font-family: "Open Sans", sans-serif; font-size: 13.5px; color: var(--ink);
  }
</style>
</head>
<body>
<main class="stage">
  <section class="card card--back" aria-label="Card back">
    <div class="map-area" role="img" aria-label="Faint world map background"></div>
    <div class="back-brand">Harbourline Freight</div>
  </section>

  <section class="card card--front" aria-label="Card front">
    <div class="map-area" role="img" aria-label="Faint world map background"></div>
    <div class="front-brand">Harbourline Freight</div>
    <div class="divider"></div>
    <div class="contact">
      <div class="contact__name">DEAN <span class="surname">FAIRLEY</span></div>
      <div class="contact__title">CEO</div>
      <div class="contact__row">
        <span class="icon-badge">
          <svg width="16" height="16" viewBox="0 0 24 24" aria-hidden="true"><path fill="#fff" d="M6.6 10.8a15.1 15.1 0 0 0 6.6 6.6l2.2-2.2a1 1 0 0 1 1-.25 11.4 11.4 0 0 0 3.6.57 1 1 0 0 1 1 1V20a1 1 0 0 1-1 1A17 17 0 0 1 3 4a1 1 0 0 1 1-1h3.5a1 1 0 0 1 1 1c0 1.25.2 2.45.57 3.6a1 1 0 0 1-.25 1z"/></svg>
        </span>
        <div><span class="contact__label">Phone:</span> 02 61847315<br><span class="contact__label">Fax:</span> 02 61847358</div>
      </div>
      <div class="contact__row">
        <span class="icon-badge">
          <svg width="16" height="16" viewBox="0 0 24 24" aria-hidden="true"><rect x="3" y="4" width="18" height="12" rx="1.5" fill="none" stroke="#fff" stroke-width="2"/><path d="M9 20h6M12 16v4" stroke="#fff" stroke-width="2"/></svg>
        </span>
        <div>dean@harbourlinefreight.example.au<br>www.harbourlinefreight.example.au</div>
      </div>
    </div>
    <div class="address">14 Wren Parade, Queanbeyan NSW 2620</div>
  </section>
</main>
</body>
</html>
```